Need Stunning Website for Talent Acquisition (Recruiting) Agency

Hello, I am seeking a very professional, high-quality website that reflects our Talent Acquisition agency, Kindred Hires. Our agency slogan is "Talent Acquisition. Differently." We are in fact different - we are a full service agency that provides services most others do not, and our website needs to immediately reflect that something is different about us when they visit our site.

This contest is to do complete website design and coding, including all graphics, features, plugins, and design elements. The graphics are very important on the site and must be of the highest professional quality. One critical aspect is that the imagery must convey that we serve clients in a variety of industries, including business, healthcare, churches and religious organizations, non-profits, manufacturing, retail, and more. We recruit for both professional level positions (e.g. CEO, COO, Pastor), as well as entry level (e.g. secretary, caregiver, factory worker).
The following pages should be designed:
Home Page - a captivating home page that immediately tells our brand story, what makes us different, and the value that we bring to the table.
Client Services Page - a page that talks more about the services we provide and why we produce better results. This page will cover the 5 C's in greater detail as well as all the things that make us different.
Industries - The industries we serve
Request Services - a page where clients can submit details about a job they would like us to recruit for, including attaching a job description if they have one
Candidates Page - a simple page that encourages prospective candidates to submit their resume for review
About Us - Common about us page
Blog - Common blog page
Contact Us - a contact page for general inquiries
The website must be built in an ultra-SEO friendly manner and optimized for speed and performance. As mentioned above, you will be responsible for providing all graphics for the site (copyright compliant).
The website will need to be compatible with Elementor Pro (I have subscription) and Yoast SEO. It needs to be designed on a high-quality wordpress theme that receives regular updates. It also needs instant chat messaging feature. Would like a traditional menu bar at the top of the page (not a fan of menu's that are hidden or put on the side of the page).

Please, please, please - - do NOT waste my time with generic/stock templates, low-quality graphics, etc. We are a PREMIUM agency and our website needs to reflect that.

In the future we will add a job board - I do not want that initially - but will want the option to add it later.

Must also have the ability to upload documents /attachments on the contact page/form.

It probably goes without saying, but the page must be fully responsive - suitable to work on all device types.

Target Market(s)

Businesses

Industry/Entity Type

Talent Acquisition (Recruiting) Agency

Coding

Coded - Design and coding required

Number of Pages Required

5+ page

Requirements
Must have
• Please see brief
Should not have
• No generic template/stock website or graphics - must have PREMIUM feel.

```html
<!DOCTYPE html>
<html lang="en">
<head>
<meta charset="utf-8">
<title>Kindred Hires – Talent Acquisition. Differently.</title>
<link href="https://fonts.googleapis.com/css2?family=Ubuntu:ital,wght@0,400;0,500;0,700;1,500&family=Open+Sans:wght@400;600;700&display=swap" rel="stylesheet">
<style>
:root{
  --navy:#141a45;
  --navy-deep:#10153a;
  --orange:#f7a21b;
  --ink:#2b2b2b;
  --muted:#6b6b6b;
  --line:#5a5f80;
  --white:#ffffff;
  --paper:#f3f3f3;
}
*{box-sizing:border-box;margin:0;padding:0}
html,body{width:728px;height:1200px;overflow:hidden;background:var(--white);font-family:"Open Sans",sans-serif;color:var(--ink)}
.page{position:absolute;top:17px;width:677px;height:2397px;transform-origin:0 0;transform:scale(0.4853);background:var(--white);overflow:hidden;box-shadow:0 0 14px rgba(0,0,0,.25)}
.page--plain{left:20px}
.page--chat{left:375.6px}
.abs{position:absolute}

/* top bar */
.topbar{left:0;top:0;width:677px;height:23px;white-space:nowrap}
.topbar__social{top:5px;width:12px;height:12px;border-radius:50%;background:var(--white)}
.topbar__mail{left:352px;top:4px;font-size:9.5px;color:var(--white);white-space:nowrap}
.topbar__chat{left:548px;top:5px;font-size:9.5px;color:var(--white);display:flex;align-items:center;gap:6px;white-space:nowrap}

/* header */
.brand{font-family:"Ubuntu",sans-serif;font-weight:700;font-size:21px;color:var(--navy);letter-spacing:-.3px;white-space:nowrap}
.header__brand{left:35px;top:30px}
.nav{left:208px;top:42px;width:440px;display:flex;justify-content:space-between;font-size:8.8px;color:var(--ink);white-space:nowrap}
.nav span{white-space:nowrap}
.nav__item--active{color:var(--orange)}

/* hero */
.hero{left:0;top:68px;width:677px;height:348px;background:linear-gradient(120deg,#6d6a66 0%,#9a938b 30%,#4c4038 55%,#8d7f72 75%,#3d3d40 100%)}
.hero__stripe{left:360px;top:68px;width:60px;height:348px;background:rgba(247,162,27,.85);clip-path:polygon(55% 0,100% 0,45% 100%,0 100%)}
.hero__title{left:0;top:208px;width:677px;text-align:center;font-family:"Ubuntu",sans-serif;font-weight:500;font-size:27px;color:var(--white);text-shadow:0 2px 6px rgba(0,0,0,.5);white-space:nowrap}
.hero__title em{font-style:italic}
.hero__scroll{left:331px;top:381px;width:16px;height:22px;border:1.5px solid var(--white);border-radius:8px}

/* headings & text */
.h2{font-family:"Ubuntu",sans-serif;font-weight:500;font-size:28px;color:var(--navy);white-space:nowrap}
.h2 span{color:var(--orange);font-weight:400}
.h2--light{color:var(--white)}
.copy{font-size:9.8px;line-height:17px;text-align:justify;color:#333}
.copy p+p{margin-top:6px}
.btn{height:30px;padding:0 12px;background:var(--orange);color:var(--white);font-size:9.5px;font-weight:700;display:flex;align-items:center;white-space:nowrap;clip-path:polygon(0 0,100% 0,94% 100%,0 100%)}
.btn-tail{width:4px;height:30px;background:var(--orange);transform:skewX(-12deg)}

/* about */
.photo{background:linear-gradient(160deg,#a9a59d,#d9c7b0 45%,#7d7468)}
.frame{border:1.5px solid var(--orange)}

/* bands */
.band{left:0;width:677px}
.ind-card{top:935px;width:167px;height:180px;border:1.5px solid var(--line);text-align:center;color:#c8cadb}
.ind-card--active{border-color:var(--orange)}
.ind-card svg{margin-top:28px}
.ind-card h3{font-family:"Ubuntu",sans-serif;font-weight:500;font-size:11.5px;color:var(--white);margin:12px 0 8px}
.ind-card p{font-size:9.8px;line-height:17px;padding:0 10px}

/* blog */
.post{top:1705px;width:160px;height:176px;background:var(--white);border-bottom:3px solid var(--orange);padding:16px 12px 0}
.post__date{font-size:8.5px;color:var(--muted)}
.post__title{font-family:"Ubuntu",sans-serif;font-size:11.5px;font-weight:500;line-height:16px;color:var(--navy);margin:9px 0 8px}
.post__text{font-size:9.5px;line-height:16px;color:#555}
.post__more{font-size:9.5px;font-weight:700;color:var(--orange);margin-top:7px}

/* footer */
.footer{left:0;top:2193px;width:677px;height:204px;background:var(--navy)}
.footer .brand{color:var(--white);font-size:20px}
.footer__col-title{font-size:8.5px;color:var(--white);letter-spacing:.2px;white-space:nowrap}
.footer__rule{width:40px;height:1.5px;background:var(--orange);margin:9px 0 12px}
.footer__links{font-size:8px;line-height:14.5px;color:#d5d7e6;white-space:nowrap}
.footer__about{font-size:8.5px;line-height:16px;color:#d5d7e6}
.footer__field{width:135px;height:28px;background:var(--white);font-size:8.5px;color:#555;padding:8px 10px}
.footer__social{width:19px;height:19px;border:1px solid var(--white);border-radius:50%}
.footer__copy{left:0;top:2382px;width:677px;text-align:center;font-size:8px;color:#d5d7e6}

/* chat */
.chat{left:416px;top:40px;width:198px;height:156px;background:var(--white);box-shadow:0 3px 10px rgba(0,0,0,.25)}
.chat__head{height:24px;background:var(--navy);color:var(--white);font-size:8.5px;font-weight:600;display:flex;align-items:center;padding-left:46px;position:relative}
.chat__avatar{width:30px;height:30px;border-radius:50%;background:var(--white);border:2px solid var(--navy)}
.chat__note{font-size:7.5px;color:#888;text-align:center;margin-top:10px;white-space:nowrap}
.chat__bubble{font-size:8px;color:#333;background:#eeeef2;padding:8px 10px;white-space:nowrap}
.chat__input{font-size:7.5px;color:#999;white-space:nowrap}
</style>
</head>
<body>

<!-- ============ PAGE : default ============ -->
<div class="page page--plain">
  <div class="abs topbar">
    <svg class="abs" width="677" height="23" style="left:0;top:0"><rect width="677" height="3" fill="#141a45"/><polygon points="245,0 505,0 505,23 262,23" fill="#141a45"/><polygon points="505,0 677,0 677,23 494,23" fill="#f7a21b"/></svg>
    <span class="abs topbar__social" style="left:267px"></span>
    <span class="abs topbar__social" style="left:294px"></span>
    <svg class="abs" style="left:334px;top:6px" width="12" height="11" viewBox="0 0 12 11"><polygon points="0,5 12,0 9,11 6,7" fill="#fff"/></svg>
    <span class="abs topbar__mail">MAIL: hello@kindredhires.com</span>
    <span class="abs topbar__chat"><svg width="12" height="12" viewBox="0 0 12 12" fill="none" stroke="#fff" stroke-width="1.4"><path d="M2 8V6a4 4 0 0 1 8 0v2"/><rect x="1" y="7" width="2.5" height="4" rx="1"/><rect x="8.5" y="7" width="2.5" height="4" rx="1"/></svg>Chat With Us</span>
  </div>
  <div class="abs brand header__brand">Kindred Hires</div>
  <nav class="abs nav"><span class="nav__item nav__item--active">Home</span><span>Client Services</span><span>Industries Served</span><span>Request Services</span><span>Candidates</span><span>Blog</span><span>About</span><span>Contact</span></nav>

  <div class="abs hero" role="img" aria-label="Photo of a recruiter interviewing a candidate in a modern lounge"></div>
  <div class="abs hero__stripe"></div>
  <h1 class="abs hero__title">Talent Acquisition. <em>Differently.</em></h1>
  <div class="abs hero__scroll"></div>

  <div class="abs frame" style="left:77px;top:479px;width:190px;height:232px"></div>
  <div class="abs photo" style="left:63px;top:494px;width:190px;height:231px" role="img" aria-label="Photo of a smiling woman working on a laptop"></div>
  <h2 class="abs h2" style="left:321px;top:494px"><span>About</span> Kindred Hires</h2>
  <div class="abs copy" style="left:321px;top:545px;width:294px">
    <p>Ut enim ad minim veniam, quis nostrud exercitation ullamco laboris nisi ut aliquip ex ea commodo consequat. Duis aute irure dolor in reprehenderit in voluptate velit esse cillum dolore eu fugiat nulla pariatur. Excepteur sint occaecat.</p>
    <p>Ut enim ad minim veniam, quis nostrud exercitation ullamco laboris nisi ut aliquip ex ea commodo consequat. Duis aute irure dolor in reprehenderit in voluptate velit esse cillum dolore.</p>
  </div>
  <div class="abs" style="left:321px;top:695px;display:flex;gap:2px"><span class="btn">LEARN MORE</span><span class="btn-tail"></span></div>

  <svg class="abs band" style="top:780px" width="677" height="450"><polygon points="0,62 677,8 677,16 0,78" fill="#f7a21b"/><polygon points="0,78 677,16 677,398 0,438" fill="#141a45"/><polygon points="0,438 677,398 677,412 0,442" fill="#f7a21b"/></svg>
  <h2 class="abs h2 h2--light" style="left:0;top:858px;width:677px;text-align:center"><span>Industries</span> We Serve</h2>
  <div class="abs ind-card" style="left:-129px"><p style="margin-top:102px;text-align:right">uris<br>e at<br>.</p></div>
  <div class="abs ind-card" style="left:63px"><svg width="40" height="40" viewBox="0 0 40 40" fill="none" stroke-width="1.6"><circle cx="14" cy="24" r="7" stroke="#fff"/><circle cx="14" cy="24" r="2.5" stroke="#fff"/><circle cx="26" cy="13" r="7" stroke="#f7a21b"/><circle cx="26" cy="13" r="2.5" stroke="#f7a21b"/></svg><h3>Manufacturing</h3><p>Duist aute irure dolor induris reprehen derit in voluptate at velit esse cillum dolore.</p></div>
  <div class="abs ind-card ind-card--active" style="left:255px"><svg width="40" height="40" viewBox="0 0 40 40" fill="none" stroke-width="1.6"><rect x="4" y="10" width="32" height="25" rx="3" stroke="#fff"/><path d="M15 10V6h10v4" stroke="#fff"/><path d="M18 17h4v4h4v4h-4v4h-4v-4h-4v-4h4z" stroke="#f7a21b"/></svg><h3>Healthcare</h3><p>Duist aute irure dolor induris reprehen derit in voluptate at velit esse cillum dolore.</p></div>
  <div class="abs ind-card" style="left:447px"><svg width="40" height="40" viewBox="0 0 40 40" fill="none" stroke-width="1.6"><path d="M20 37C11 27 7 21 7 15a13 13 0 0 1 26 0c0 6-4 12-13 22z" stroke="#fff"/><path d="M20 9v13M15 14h10" stroke="#f7a21b"/></svg><h3>Churches</h3><p>Duist aute irure dolor induris reprehen derit in voluptate at velit esse cillum dolore.</p></div>
  <div class="abs ind-card" style="left:639px"><p style="margin-top:102px;text-align:left">Duist<br>repre<br>ve</p></div>

  <h2 class="abs h2" style="left:62px;top:1274px"><span>Why</span> We're Better</h2>
  <div class="abs copy" style="left:62px;top:1320px;width:294px">
    <p>Ut enim ad minim veniam, quis nostrud exercitation ullamco laboris nisi ut aliquip ex ea commodo consequat. Duis aute irure dolor in reprehenderit in voluptate velit esse cillum dolore eu fugiat nulla pariatur. Excepteur sint occaecat.</p>
    <p>Ut enim ad minim veniam, quis nostrud exercitation ullamco laboris nisi ut aliquip ex ea commodo consequat. Duis aute irure dolor in reprehenderit in voluptate velit esse cillum dolore.</p>
  </div>
  <div class="abs" style="left:62px;top:1465px;display:flex;gap:2px"><span class="btn">UPLOAD RESUME</span><span class="btn-tail"></span></div>
  <svg class="abs" style="left:400px;top:1258px" width="220" height="260" fill="none" stroke="#f7a21b" stroke-width="1.5"><path d="M150 1h63v120"/><path d="M3 190v68h65"/></svg>
  <div class="abs photo" style="left:418px;top:1269px;width:189px;height:231px;background:linear-gradient(150deg,#8f98a3,#5f6670 45%,#2e4a78)" role="img" aria-label="Photo of two businessmen shaking hands"></div>

  <svg class="abs band" style="top:1565px" width="677" height="400"><polygon points="0,18 677,0 677,8 0,30" fill="#f7a21b"/><polygon points="0,30 677,8 677,352 0,388" fill="#141a45"/><polygon points="0,388 677,352 677,366 0,392" fill="#f7a21b"/></svg>
  <h2 class="abs h2 h2--light" style="left:0;top:1633px;width:677px;text-align:center"><span>Our</span> Blog</h2>
  <div class="abs post" style="left:82px"><div class="post__date">02-06-2022</div><div class="post__title">Duis aute irure dolor volt incieri rnderit in volupt.</div><div class="post__text">Duis aute irure dolor voltter incieri rnderit in volupt. Cillt dolore eu fugiat nulla loreti pariatur.</div><div class="post__more">READ MORE</div></div>
  <div class="abs post" style="left:258px"><div class="post__date">02-06-2022</div><div class="post__title">Duis aute irure dolor volt incieri rnderit in volupt.</div><div class="post__text">Duis aute irure dolor voltter incieri rnderit in volupt. Cillt dolore eu fugiat nulla loreti pariatur.</div><div class="post__more">READ MORE</div></div>
  <div class="abs post" style="left:435px"><div class="post__date">02-06-2022</div><div class="post__title">Duis aute irure dolor volt incieri rnderit in volupt.</div><div class="post__text">Duis aute irure dolor voltter incieri rnderit in volupt. Cillt dolore eu fugiat nulla loreti pariatur.</div><div class="post__more">READ MORE</div></div>

  <h2 class="abs h2" style="left:0;top:2006px;width:677px;text-align:center"><span>Our</span> Candidates</h2>
  <div class="abs copy" style="left:96px;top:2056px;width:486px;text-align:center">Ut enim ad minim veniam, quis nostrud exercitation ullamco laboris nisi ut aliquip ex ea commodo consequat. Duis aute irure dolor in reprehenderit in voluptate velit esse cillum dolore eu fugiat nulla pariatur. Excepteur sint occaecat.</div>
  <div class="abs" style="left:293px;top:2133px;display:flex;gap:2px"><span class="btn">LEARN MORE</span><span class="btn-tail"></span></div>

  <footer class="abs footer">
    <div class="abs brand" style="left:63px;top:32px">Kindred Hires</div>
    <div class="abs footer__about" style="left:63px;top:70px;width:170px">Sed ut perspiciatis unde omnis lotr iste natus error sit voluptatem littero accusantium dolore laudantium.</div>
    <div class="abs" style="left:63px;top:142px;display:flex;align-items:center;gap:6px;font-size:9px;color:#fff;white-space:nowrap">FOLLOW US: <span class="footer__social"></span><span class="footer__social"></span></div>
    <div class="abs" style="left:273px;top:36px"><div class="footer__col-title">QUICK LINKS</div><div class="footer__rule"></div><div class="footer__links">Home<br>Client Services<br>Industries<br>Request Services<br>Candidate</div></div>
    <div class="abs" style="left:382px;top:36px"><div class="footer__col-title">OTHER LINKS</div><div class="footer__rule"></div><div class="footer__links">About Us<br>Blog<br>Contact Us</div></div>
    <div class="abs" style="left:479px;top:36px"><div class="footer__col-title">NEWSLETTER SIGNUP</div><div class="footer__field" style="margin-top:20px">Email ID</div><div style="margin-top:8px;display:flex;gap:2px"><span class="btn" style="height:24px;font-weight:600">Learn More</span><span class="btn-tail" style="height:24px"></span></div></div>
    <div class="abs" style="left:63px;top:172px;width:551px;height:1px;background:#3a3f66"></div>
  </footer>
  <div class="abs footer__copy">©Copyrights 2022 Kindred Hires. All Rights Reserved.</div>
</div>

<!-- ============ PAGE : chat open ============ -->
<div class="page page--chat">
  <div class="abs topbar">
    <svg class="abs" width="677" height="23" style="left:0;top:0"><rect width="677" height="3" fill="#141a45"/><polygon points="245,0 505,0 505,23 262,23" fill="#141a45"/><polygon points="505,0 677,0 677,23 494,23" fill="#f7a21b"/></svg>
    <span class="abs topbar__social" style="left:267px"></span>
    <span class="abs topbar__social" style="left:294px"></span>
    <svg class="abs" style="left:334px;top:6px" width="12" height="11" viewBox="0 0 12 11"><polygon points="0,5 12,0 9,11 6,7" fill="#fff"/></svg>
    <span class="abs topbar__mail">MAIL: hello@kindredhires.com</span>
    <span class="abs topbar__chat"><svg width="12" height="12" viewBox="0 0 12 12" fill="none" stroke="#fff" stroke-width="1.4"><path d="M2 8V6a4 4 0 0 1 8 0v2"/><rect x="1" y="7" width="2.5" height="4" rx="1"/><rect x="8.5" y="7" width="2.5" height="4" rx="1"/></svg>Chat With Us</span>
  </div>
  <div class="abs brand header__brand">Kindred Hires</div>
  <nav class="abs nav"><span class="nav__item nav__item--active">Home</span><span>Client Services</span><span>Industries Served</span><span>Request Services</span><span>Candidates</span><span>Blog</span><span>About</span><span>Contact</span></nav>

  <div class="abs hero" role="img" aria-label="Photo of a recruiter interviewing a candidate in a modern lounge"></div>
  <div class="abs hero__stripe"></div>
  <h1 class="abs hero__title">Talent Acquisition. <em>Differently.</em></h1>
  <div class="abs hero__scroll"></div>

  <div class="abs chat">
    <div class="chat__head">Support<span style="position:absolute;right:10px;font-size:11px;font-weight:400">×</span></div>
    <div class="abs chat__avatar" style="left:8px;top:-6px"></div>
    <div class="chat__note">KH Support has joined the chat.</div>
    <div style="display:flex;align-items:center;gap:10px;margin:18px 0 0 14px"><span style="width:20px;height:20px;border-radius:50%;border:1px solid #ddd"></span><span class="chat__bubble">Hellow, how may I help you?</span></div>
    <div style="position:absolute;left:0;top:122px;width:198px;height:1px;background:#e6e6e6"></div>
    <div class="abs chat__input" style="left:12px;top:134px">Type your message here</div>
  </div>

  <div class="abs frame" style="left:77px;top:479px;width:190px;height:232px"></div>
  <div class="abs photo" style="left:63px;top:494px;width:190px;height:231px" role="img" aria-label="Photo of a smiling woman working on a laptop"></div>
  <h2 class="abs h2" style="left:321px;top:494px"><span>About</span> Kindred Hires</h2>
  <div class="abs copy" style="left:321px;top:545px;width:294px">
    <p>Ut enim ad minim veniam, quis nostrud exercitation ullamco laboris nisi ut aliquip ex ea commodo consequat. Duis aute irure dolor in reprehenderit in voluptate velit esse cillum dolore eu fugiat nulla pariatur. Excepteur sint occaecat.</p>
    <p>Ut enim ad minim veniam, quis nostrud exercitation ullamco laboris nisi ut aliquip ex ea commodo consequat. Duis aute irure dolor in reprehenderit in voluptate velit esse cillum dolore.</p>
  </div>
  <div class="abs" style="left:321px;top:695px;display:flex;gap:2px"><span class="btn">LEARN MORE</span><span class="btn-tail"></span></div>

  <svg class="abs band" style="top:780px" width="677" height="450"><polygon points="0,62 677,8 677,16 0,78" fill="#f7a21b"/><polygon points="0,78 677,16 677,398 0,438" fill="#141a45"/><polygon points="0,438 677,398 677,412 0,442" fill="#f7a21b"/></svg>
  <h2 class="abs h2 h2--light" style="left:0;top:858px;width:677px;text-align:center"><span>Industries</span> We Serve</h2>
  <div class="abs ind-card" style="left:-129px"><p style="margin-top:102px;text-align:right">uris<br>e at<br>.</p></div>
  <div class="abs ind-card" style="left:63px"><svg width="40" height="40" viewBox="0 0 40 40" fill="none" stroke-width="1.6"><circle cx="14" cy="24" r="7" stroke="#fff"/><circle cx="14" cy="24" r="2.5" stroke="#fff"/><circle cx="26" cy="13" r="7" stroke="#f7a21b"/><circle cx="26" cy="13" r="2.5" stroke="#f7a21b"/></svg><h3>Manufacturing</h3><p>Duist aute irure dolor induris reprehen derit in voluptate at velit esse cillum dolore.</p></div>
  <div class="abs ind-card ind-card--active" style="left:255px"><svg width="40" height="40" viewBox="0 0 40 40" fill="none" stroke-width="1.6"><rect x="4" y="10" width="32" height="25" rx="3" stroke="#fff"/><path d="M15 10V6h10v4" stroke="#fff"/><path d="M18 17h4v4h4v4h-4v4h-4v-4h-4v-4h4z" stroke="#f7a21b"/></svg><h3>Healthcare</h3><p>Duist aute irure dolor induris reprehen derit in voluptate at velit esse cillum dolore.</p></div>
  <div class="abs ind-card" style="left:447px"><svg width="40" height="40" viewBox="0 0 40 40" fill="none" stroke-width="1.6"><path d="M20 37C11 27 7 21 7 15a13 13 0 0 1 26 0c0 6-4 12-13 22z" stroke="#fff"/><path d="M20 9v13M15 14h10" stroke="#f7a21b"/></svg><h3>Churches</h3><p>Duist aute irure dolor induris reprehen derit in voluptate at velit esse cillum dolore.</p></div>
  <div class="abs ind-card" style="left:639px"><p style="margin-top:102px;text-align:left">Duist<br>repre<br>ve</p></div>

  <h2 class="abs h2" style="left:62px;top:1274px"><span>Why</span> We're Better</h2>
  <div class="abs copy" style="left:62px;top:1320px;width:294px">
    <p>Ut enim ad minim veniam, quis nostrud exercitation ullamco laboris nisi ut aliquip ex ea commodo consequat. Duis aute irure dolor in reprehenderit in voluptate velit esse cillum dolore eu fugiat nulla pariatur. Excepteur sint occaecat.</p>
    <p>Ut enim ad minim veniam, quis nostrud exercitation ullamco laboris nisi ut aliquip ex ea commodo consequat. Duis aute irure dolor in reprehenderit in voluptate velit esse cillum dolore.</p>
  </div>
  <div class="abs" style="left:62px;top:1465px;display:flex;gap:2px"><span class="btn">UPLOAD RESUME</span><span class="btn-tail"></span></div>
  <svg class="abs" style="left:400px;top:1258px" width="220" height="260" fill="none" stroke="#f7a21b" stroke-width="1.5"><path d="M150 1h63v120"/><path d="M3 190v68h65"/></svg>
  <div class="abs photo" style="left:418px;top:1269px;width:189px;height:231px;background:linear-gradient(150deg,#8f98a3,#5f6670 45%,#2e4a78)" role="img" aria-label="Photo of two businessmen shaking hands"></div>

  <svg class="abs band" style="top:1565px" width="677" height="400"><polygon points="0,18 677,0 677,8 0,30" fill="#f7a21b"/><polygon points="0,30 677,8 677,352 0,388" fill="#141a45"/><polygon points="0,388 677,352 677,366 0,392" fill="#f7a21b"/></svg>
  <h2 class="abs h2 h2--light" style="left:0;top:1633px;width:677px;text-align:center"><span>Our</span> Blog</h2>
  <div class="abs post" style="left:82px"><div class="post__date">02-06-2022</div><div class="post__title">Duis aute irure dolor volt incieri rnderit in volupt.</div><div class="post__text">Duis aute irure dolor voltter incieri rnderit in volupt. Cillt dolore eu fugiat nulla loreti pariatur.</div><div class="post__more">READ MORE</div></div>
  <div class="abs post" style="left:258px"><div class="post__date">02-06-2022</div><div class="post__title">Duis aute irure dolor volt incieri rnderit in volupt.</div><div class="post__text">Duis aute irure dolor voltter incieri rnderit in volupt. Cillt dolore eu fugiat nulla loreti pariatur.</div><div class="post__more">READ MORE</div></div>
  <div class="abs post" style="left:435px"><div class="post__date">02-06-2022</div><div class="post__title">Duis aute irure dolor volt incieri rnderit in volupt.</div><div class="post__text">Duis aute irure dolor voltter incieri rnderit in volupt. Cillt dolore eu fugiat nulla loreti pariatur.</div><div class="post__more">READ MORE</div></div>

  <h2 class="abs h2" style="left:0;top:2006px;width:677px;text-align:center"><span>Our</span> Candidates</h2>
  <div class="abs copy" style="left:96px;top:2056px;width:486px;text-align:center">Ut enim ad minim veniam, quis nostrud exercitation ullamco laboris nisi ut aliquip ex ea commodo consequat. Duis aute irure dolor in reprehenderit in voluptate velit esse cillum dolore eu fugiat nulla pariatur. Excepteur sint occaecat.</div>
  <div class="abs" style="left:293px;top:2133px;display:flex;gap:2px"><span class="btn">LEARN MORE</span><span class="btn-tail"></span></div>

  <footer class="abs footer">
    <div class="abs brand" style="left:63px;top:32px">Kindred Hires</div>
    <div class="abs footer__about" style="left:63px;top:70px;width:170px">Sed ut perspiciatis unde omnis lotr iste natus error sit voluptatem littero accusantium dolore laudantium.</div>
    <div class="abs" style="left:63px;top:142px;display:flex;align-items:center;gap:6px;font-size:9px;color:#fff;white-space:nowrap">FOLLOW US: <span class="footer__social"></span><span class="footer__social"></span></div>
    <div class="abs" style="left:273px;top:36px"><div class="footer__col-title">QUICK LINKS</div><div class="footer__rule"></div><div class="footer__links">Home<br>Client Services<br>Industries<br>Request Services<br>Candidate</div></div>
    <div class="abs" style="left:382px;top:36px"><div class="footer__col-title">OTHER LINKS</div><div class="footer__rule"></div><div class="footer__links">About Us<br>Blog<br>Contact Us</div></div>
    <div class="abs" style="left:479px;top:36px"><div class="footer__col-title">NEWSLETTER SIGNUP</div><div class="footer__field" style="margin-top:20px">Email ID</div><div style="margin-top:8px;display:flex;gap:2px"><span class="btn" style="height:24px;font-weight:600">Learn More</span><span class="btn-tail" style="height:24px"></span></div></div>
    <div class="abs" style="left:63px;top:172px;width:551px;height:1px;background:#3a3f66"></div>
  </footer>
  <div class="abs footer__copy">©Copyrights 2022 Kindred Hires. All Rights Reserved.</div>
</div>

</body>
</html>
```